Talent Management Company Needs Business Cards

Using one of the logos provided (attached) K&R Talent Collective needs a business card designed.
Please visit our website for more information about us-

www.krtalentcollective.example

The face should feature a dramatic presentation of the logo with the back being reserved for our professional information which is:

The information should be:
Dorian T. Vickers
C.E.O
Email: dtvickers@krtalentcollective.example
Mobile: 555-804-2917
Website: www.krtalentcollective.example

Marcus L. Vickers
Director of Public Relations
Email: mlvickers@krtalentcollective.example
Mobile: 555-806-3350

Jules R. Hampton
Director of Client Development
Email: jhampton@krtalentcollective.example

Simon Hurlock
Director of Brand Development
Email: shurlock@krtalentcollective.example

Would like the logo to have color. I would like to see one side red or black and the other side white but if it looks better in either black or red that would be fine to but would like to see how it comes out.

Please feel free to message me and if you would like just the icon alone I have other image files that I can send as well.

Target Market(s)

Professional Athletes, coaches, entertainers age 18-35 but also must be accepted in the business community

Industry/Entity Type

Business

Requirements
Must have
• 1) Use the logo
2) Double sided
3) Distinctive
Nice to have
• Small simple images for telephone, e-mail, and Url.

```html
<!DOCTYPE html>
<html lang="en">
<head>
<meta charset="utf-8">
<title>K&amp;R Talent Collective — Business Card</title>
<link rel="stylesheet" href="https://fonts.googleapis.com/css2?family=Open+Sans:wght@400;600;700&display=swap">
<style>
  :root {
    --backdrop: #3b3b3b;
    --card-black: #000000;
    --brand-red: #ec1c24;
    --ink-white: #ffffff;
  }
  html, body {
    margin: 0;
    padding: 0;
    width: 1200px;
    height: 501px;
    overflow: hidden;
    background: var(--backdrop);
    font-family: "Open Sans", Arial, sans-serif;
  }
  .stage {
    position: relative;
    width: 1200px;
    height: 501px;
  }
  .card {
    position: absolute;
    top: 93px;
    width: 528px;
    height: 316px;
    background: var(--card-black);
    overflow: hidden;
    box-shadow: 0 4px 14px rgba(0,0,0,0.45);
  }
  .card--front { left: 47px; }
  .card--back { left: 623px; }
  .card__band {
    position: absolute;
    left: 0;
    right: 0;
    bottom: 0;
    height: 40px;
    background: var(--brand-red);
  }
  .brand-mark {
    position: absolute;
    left: 50%;
    top: 40px;
    width: 78px;
    height: 78px;
    margin-left: -39px;
    border-radius: 50%;
    background: var(--brand-red);
  }
  .brand-name {
    position: absolute;
    left: 0;
    right: 0;
    top: 170px;
    text-align: center;
    color: var(--ink-white);
    font-weight: 400;
    font-size: 30px;
    letter-spacing: 0.5px;
    white-space: nowrap;
  }
  .contact-name {
    position: absolute;
    left: 34px;
    top: 10px;
    margin: 0;
    color: var(--ink-white);
    font-weight: 600;
    font-size: 37px;
    letter-spacing: -0.3px;
    white-space: nowrap;
  }
  .contact-title {
    position: absolute;
    left: 80px;
    top: 62px;
    color: var(--brand-red);
    font-weight: 400;
    font-size: 16px;
  }
  .contact-brand {
    position: absolute;
    left: 80px;
    top: 90px;
    color: var(--ink-white);
    font-weight: 600;
    font-size: 9px;
    letter-spacing: 0.6px;
    white-space: nowrap;
  }
  .contact-strips {
    position: absolute;
    left: 0;
    top: 0;
    width: 528px;
    height: 316px;
  }
  .strip { fill: var(--brand-red); }
  .strip-text {
    fill: var(--ink-white);
    font-family: "Open Sans", Arial, sans-serif;
    font-size: 10.5px;
  }
  .icon-disc { fill: var(--ink-white); }
  .icon-glyph { fill: var(--brand-red); stroke: var(--brand-red); }
</style>
</head>
<body>
<main class="stage">

  <section class="card card--front" aria-label="Card front">
    <div class="brand-mark"></div>
    <div class="brand-name">K&amp;R TALENT COLLECTIVE</div>
    <div class="card__band"></div>
  </section>

  <section class="card card--back" aria-label="Card back">
    <h1 class="contact-name">Dorian T. Vickers</h1>
    <div class="contact-title">C.E.O</div>
    <div class="contact-brand">K&amp;R TALENT COLLECTIVE</div>

    <svg class="contact-strips" viewBox="0 0 528 316" xmlns="http://www.w3.org/2000/svg">
      <polygon class="strip" points="72,276 484,70 484,92 116,276"/>
      <polygon class="strip" points="152,276 464,120 464,142 196,276"/>
      <polygon class="strip" points="238,276 404,193 404,215 282,276"/>

      <g transform="translate(250 198) rotate(-26.57)">
        <circle class="icon-disc" cx="0" cy="0" r="7"/>
        <rect x="-4" y="-3" width="8" height="6" fill="none" class="icon-glyph" stroke-width="1"/>
        <polyline points="-4,-3 0,0.5 4,-3" fill="none" class="icon-glyph" stroke-width="1"/>
        <text class="strip-text" x="12" y="4">dtvickers@krtalentcollective.example</text>
      </g>

      <g transform="translate(270 228) rotate(-26.57)">
        <circle class="icon-disc" cx="0" cy="0" r="7"/>
        <circle cx="0" cy="0" r="4.5" fill="none" class="icon-glyph" stroke-width="1"/>
        <line x1="-4.5" y1="0" x2="4.5" y2="0" class="icon-glyph" stroke-width="0.8"/>
        <ellipse cx="0" cy="0" rx="2" ry="4.5" fill="none" class="icon-glyph" stroke-width="0.8"/>
        <text class="strip-text" x="12" y="4">www.krtalentcollective.example</text>
      </g>

      <g transform="translate(290 261) rotate(-26.57)">
        <circle class="icon-disc" cx="0" cy="0" r="7"/>
        <path class="icon-glyph" stroke="none" d="M-3.5,-4 L-1.5,-4.5 L-0.5,-2 L-1.8,-1 Q-1,1 1,1.8 L2,0.5 L4.5,1.5 L4,3.5 Q-3.5,4 -3.5,-4 Z"/>
        <text class="strip-text" x="12" y="4">555-804-2917</text>
      </g>
    </svg>

    <div class="card__band"></div>
  </section>

</main>
</body>
</html>
```